Homeopathic medicinal cream label design

I am looking for a product label design for a medicinal (cannabis) topical cream to be sold to medical marijuana patients. It is a new product that has not yet established a brand identity. It will be sold in 2 and 4 ounce containers so the design needs to work on a small scale. The design may be used for other branding as well.

Target Market(s)

Medical marijuana users in states where it is legal. The product should appeal to both men and women to promote pain relief in muscles and joints. It can also be used as a massage cream for general relaxation.

Industry/Entity Type

Medical

Font styles to use
Sans Serif

Requirements
Must have
• Something that reflects the company name - The Quiet Lark - and the name of the initial product - Meadow Balm Blend.
• In addition to the name of the company and the name of the product, other information to include would be the volume being sold (e.g. 4 oz.), that it is a topical botanical ointment, and its ingredients (coconut oil, beeswax, soy lecithin, and eight all natural botanical oils - cannabis, lavender, eucalyptus, peppermint, rosemary, cinnamon, clove, and lemon). The label should clearly state that the product is for topical use only.
• The information must fit on the space available on the package. The 4 oz. container's lid has approximately 2 1/8" of surface area. The width of the label on the lid should be approximately 1 7/8". On the container's body, the height of the surface area is approximately 1", and the width is approximately 8 1/2 inches. The width of the label should be around 8 inches to allow room for it to be applied to the container. I have posted a photo of the 4 oz. container and the 2 oz. container. I have also posted a photo of the labeling of some of our competitors with similar products.
Nice to have
• We are thinking of having the logo on the lid of the container, and a circle bordering the lid that may have text in it. (See the "Amber Owl" label attached as an exemplar).
• The label on the body of the container (or maybe on the bottom on the container) would list other information about the product, such as its ingredients and our contact information.

```html
<!DOCTYPE html>
<html lang="en">
<head>
<meta charset="utf-8">
<title>Meadow Balm Blend – Label System</title>
<link href="https://fonts.googleapis.com/css2?family=Raleway:wght@400;600;700&display=swap" rel="stylesheet">
<style>
  :root {
    --page: #f4efef;
    --white: #ffffff;
    --green: #1f8a45;
    --taupe: #8f8878;
    --maroon: #7a2c2f;
    --leaf: #45b03c;
  }
  html, body {
    margin: 0;
    padding: 0;
    width: 1200px;
    height: 840px;
    overflow: hidden;
    background: var(--page);
    font-family: "Raleway", sans-serif;
  }
  .canvas { position: relative; width: 1200px; height: 840px; }
  .lid-row {
    position: absolute;
    top: 36px;
    left: 0;
    width: 1200px;
    display: flex;
    justify-content: center;
    gap: 120px;
  }
  .lid { width: 240px; height: 240px; display: block; }
  .body-stack {
    position: absolute;
    top: 318px;
    left: 50px;
    display: flex;
    flex-direction: column;
    gap: 32px;
  }
  .body-label { width: 1100px; height: 138px; display: block; }

  .tone-green  { --tone: var(--green); }
  .tone-taupe  { --tone: var(--taupe); }
  .tone-maroon { --tone: var(--maroon); }

  .tone-fill { fill: var(--tone); }
  .tone-stroke { stroke: var(--tone); }
  .tone-text { fill: var(--tone); }
  .white-text { fill: var(--white); }
  .ring-text { font-size: 11px; font-weight: 400; letter-spacing: 0.6px; }
  .lid-title { font-size: 22px; font-weight: 700; }
  .brand-name { font-size: 12px; font-weight: 400; letter-spacing: 0.3px; }
  .body-title { font-size: 26px; font-weight: 600; letter-spacing: 0.2px; }
  .body-volume { font-size: 11px; font-weight: 400; }
  .side-title { font-size: 9px; font-weight: 600; }
  .side-small { font-size: 7px; font-weight: 400; }
</style>
</head>
<body>
<main class="canvas">

  <section class="lid-row">
    <svg class="lid tone-green" viewBox="0 0 240 240" aria-label="Lid label, green">
      <defs>
        <path id="ring-a" d="M120,120 m-100,0 a100,100 0 1,1 200,0 a100,100 0 1,1 -200,0"/>
        <path id="arc-a" d="M48,122 A72,72 0 0,1 192,122"/>
      </defs>
      <circle cx="120" cy="120" r="116" fill="var(--white)" class="tone-stroke" stroke-width="3"/>
      <circle cx="120" cy="120" r="90" fill="none" class="tone-stroke" stroke-width="1"/>
      <text class="ring-text tone-text"><textPath href="#ring-a" startOffset="2%">Topical botanical ointment • Topical botanical ointment •</textPath></text>
      <text class="lid-title tone-text" text-anchor="middle"><textPath href="#arc-a" startOffset="50%">Meadow Balm Blend</textPath></text>
      <circle cx="120" cy="130" r="9" class="tone-fill"/>
      <text class="brand-name tone-text" x="120" y="160" text-anchor="middle">the quiet lark</text>
      <rect x="104" y="172" width="32" height="30" rx="10" fill="var(--leaf)" role="img" aria-label="Small botanical leaf illustration"/>
    </svg>

    <svg class="lid tone-taupe" viewBox="0 0 240 240" aria-label="Lid label, taupe">
      <defs>
        <path id="ring-b" d="M120,120 m-100,0 a100,100 0 1,1 200,0 a100,100 0 1,1 -200,0"/>
        <path id="arc-b" d="M48,122 A72,72 0 0,1 192,122"/>
      </defs>
      <circle cx="120" cy="120" r="116" fill="var(--white)" class="tone-stroke" stroke-width="3"/>
      <circle cx="120" cy="120" r="90" fill="none" class="tone-stroke" stroke-width="1"/>
      <text class="ring-text tone-text"><textPath href="#ring-b" startOffset="2%">Topical botanical ointment • Topical botanical ointment •</textPath></text>
      <text class="lid-title tone-text" text-anchor="middle"><textPath href="#arc-b" startOffset="50%">Meadow Balm Blend</textPath></text>
      <circle cx="120" cy="130" r="9" class="tone-fill"/>
      <text class="brand-name tone-text" x="120" y="160" text-anchor="middle">the quiet lark</text>
      <rect x="104" y="172" width="32" height="30" rx="10" fill="var(--leaf)" role="img" aria-label="Small botanical leaf illustration"/>
    </svg>

    <svg class="lid tone-maroon" viewBox="0 0 240 240" aria-label="Lid label, maroon">
      <defs>
        <path id="ring-c" d="M120,120 m-100,0 a100,100 0 1,1 200,0 a100,100 0 1,1 -200,0"/>
        <path id="arc-c" d="M48,122 A72,72 0 0,1 192,122"/>
      </defs>
      <circle cx="120" cy="120" r="116" fill="var(--white)" class="tone-stroke" stroke-width="3"/>
      <circle cx="120" cy="120" r="90" fill="none" class="tone-stroke" stroke-width="1"/>
      <text class="ring-text tone-text"><textPath href="#ring-c" startOffset="2%">Topical botanical ointment • Topical botanical ointment •</textPath></text>
      <text class="lid-title tone-text" text-anchor="middle"><textPath href="#arc-c" startOffset="50%">Meadow Balm Blend</textPath></text>
      <circle cx="120" cy="130" r="9" class="tone-fill"/>
      <text class="brand-name tone-text" x="120" y="160" text-anchor="middle">the quiet lark</text>
      <rect x="104" y="172" width="32" height="30" rx="10" fill="var(--leaf)" role="img" aria-label="Small botanical leaf illustration"/>
    </svg>
  </section>

  <section class="body-stack">
    <svg class="body-label tone-green" viewBox="0 0 1100 138" aria-label="Body wrap label, green">
      <rect width="1100" height="138" class="tone-fill"/>
      <rect width="1100" height="138" fill="var(--white)" opacity="0.06" role="img" aria-label="Faint botanical leaf pattern"/>
      <circle cx="375" cy="18" r="6" fill="var(--white)"/>
      <text class="brand-name white-text" x="375" y="42" text-anchor="middle">the quiet lark</text>
      <text class="body-title white-text" x="375" y="78" text-anchor="middle">MEADOW BALM BLEND</text>
      <rect x="355" y="88" width="40" height="20" rx="8" fill="var(--leaf)" role="img" aria-label="Botanical leaf illustration"/>
      <text class="body-volume white-text" x="375" y="126" text-anchor="middle">4 oz (118 ml)</text>
      <g transform="translate(760,69) rotate(90)">
        <text class="side-title white-text" x="0" y="0" text-anchor="middle">MEADOW BALM BLEND</text>
        <text class="side-small white-text" x="0" y="-16" text-anchor="middle">the quiet lark</text>
        <text class="side-small white-text" x="0" y="-28" text-anchor="middle">4 oz (118 ml)</text>
      </g>
    </svg>

    <svg class="body-label tone-taupe" viewBox="0 0 1100 138" aria-label="Body wrap label, taupe">
      <rect width="1100" height="138" class="tone-fill"/>
      <rect width="1100" height="138" fill="var(--white)" opacity="0.06" role="img" aria-label="Faint botanical leaf pattern"/>
      <circle cx="375" cy="18" r="6" fill="var(--white)"/>
      <text class="brand-name white-text" x="375" y="42" text-anchor="middle">the quiet lark</text>
      <text class="body-title white-text" x="375" y="78" text-anchor="middle">MEADOW BALM BLEND</text>
      <rect x="355" y="88" width="40" height="20" rx="8" fill="var(--leaf)" role="img" aria-label="Botanical leaf illustration"/>
      <text class="body-volume white-text" x="375" y="126" text-anchor="middle">4 oz (118 ml)</text>
      <g transform="translate(760,69) rotate(90)">
        <text class="side-title white-text" x="0" y="0" text-anchor="middle">MEADOW BALM BLEND</text>
        <text class="side-small white-text" x="0" y="-16" text-anchor="middle">the quiet lark</text>
        <text class="side-small white-text" x="0" y="-28" text-anchor="middle">4 oz (118 ml)</text>
      </g>
    </svg>

    <svg class="body-label tone-maroon" viewBox="0 0 1100 138" aria-label="Body wrap label, maroon">
      <rect width="1100" height="138" class="tone-fill"/>
      <rect width="1100" height="138" fill="var(--white)" opacity="0.06" role="img" aria-label="Faint botanical leaf pattern"/>
      <circle cx="375" cy="18" r="6" fill="var(--white)"/>
      <text class="brand-name white-text" x="375" y="42" text-anchor="middle">the quiet lark</text>
      <text class="body-title white-text" x="375" y="78" text-anchor="middle">MEADOW BALM BLEND</text>
      <rect x="355" y="88" width="40" height="20" rx="8" fill="var(--leaf)" role="img" aria-label="Botanical leaf illustration"/>
      <text class="body-volume white-text" x="375" y="126" text-anchor="middle">4 oz (118 ml)</text>
      <g transform="translate(760,69) rotate(90)">
        <text class="side-title white-text" x="0" y="0" text-anchor="middle">MEADOW BALM BLEND</text>
        <text class="side-small white-text" x="0" y="-16" text-anchor="middle">the quiet lark</text>
        <text class="side-small white-text" x="0" y="-28" text-anchor="middle">4 oz (118 ml)</text>
      </g>
    </svg>
  </section>

</main>
</body>
</html>
```